Larkspur Ridge Management - Business Cards

I need business cards. My current logo was designed by a designer at this site and I very much like and am happy with the results. I would like a business card that is trendy, unique, current yet professional. I deal with high net worth clients daily

Target Market(s)

Out of state investors looking to get into the rental market in Ohio

Industry/Entity Type

Property Management, Consulting

Contact Information for Business Card

Name, Title (Chief Financial Officer) office phone number (555) 817-3094 website address larkridgemgmt.example

Font styles to use
Sans Serif

Colors
0054AA
0677BA
7BADD7
CADEEF
E8F1F8
0094D4
00A9DD
6FCCEA
C7EBF8
E9F6FB
00AB8E
00BBA5
67D7C9
C6EFE9
E9F9F6

```html
<!DOCTYPE html>
<html lang="en">
<head>
<meta charset="utf-8">
<title>Larkspur Ridge Management – Business Card</title>
<link rel="stylesheet" href="https://fonts.googleapis.com/css2?family=Montserrat:wght@700;800&family=Mulish:ital,wght@0,400;1,400&display=swap">
<style>
  :root {
    --navy: #233659;
    --red: #c8292f;
    --red-dark: #a01f25;
    --sky: #cadeef;
    --line-blue: #2b8ed0;
    --text-gray: #555b63;
    --page: #e6e8eb;
    --white: #ffffff;
  }
  * { box-sizing: border-box; margin: 0; padding: 0; }
  html, body {
    width: 1200px;
    height: 720px;
    overflow: hidden;
    background: var(--page);
  }
  .card {
    position: absolute;
    left: 40px;
    top: 40px;
    width: 1050px;
    height: 600px;
    background: var(--white);
    transform: scale(1.066667);
    transform-origin: top left;
    overflow: hidden;
  }
  .card-graphics {
    position: absolute;
    inset: 0;
    width: 1050px;
    height: 600px;
  }
  .identity {
    position: absolute;
    left: 70px;
    top: 106px;
  }
  .person-name {
    font-family: "Montserrat", sans-serif;
    font-weight: 800;
    font-size: 42px;
    letter-spacing: -0.3px;
    color: var(--navy);
    line-height: 1;
  }
  .person-title {
    font-family: "Mulish", sans-serif;
    font-weight: 400;
    font-size: 27px;
    color: var(--text-gray);
    margin-top: 8px;
    line-height: 1;
  }
  .title-rule {
    width: 206px;
    height: 3px;
    background: var(--line-blue);
    margin-top: 22px;
  }
  .tagline {
    font-family: "Mulish", sans-serif;
    font-style: italic;
    font-size: 23px;
    color: var(--text-gray);
    margin-top: 26px;
  }
  .company-mark {
    position: absolute;
    left: 690px;
    top: 250px;
    width: 280px;
    display: flex;
    align-items: center;
    gap: 14px;
    background: var(--white);
    padding: 18px 16px;
  }
  .company-mark .mark-square {
    flex: none;
    width: 34px;
    height: 34px;
    background: var(--red);
  }
  .company-mark .company-name {
    font-family: "Montserrat", sans-serif;
    font-weight: 800;
    font-size: 27px;
    line-height: 1.1;
    color: var(--navy);
  }
  .contact-line {
    position: absolute;
    right: 52px;
    top: 522px;
    display: flex;
    align-items: center;
    gap: 13px;
    font-family: "Montserrat", sans-serif;
    font-weight: 700;
    font-size: 25px;
    white-space: nowrap;
    color: var(--navy);
  }
  .contact-line .divider-star {
    width: 20px;
    height: 20px;
  }
</style>
</head>
<body>
  <div class="card">
    <svg class="card-graphics" viewBox="0 0 1050 600" aria-hidden="true">
      <polygon fill="var(--sky)" points="283,0 1050,0 1050,396 684,27 283,27"/>
      <line x1="805" y1="0" x2="1050" y2="238" stroke="var(--line-blue)" stroke-width="2"/>
      <line x1="960" y1="0" x2="1050" y2="87" stroke="var(--line-blue)" stroke-width="2"/>
      <polyline fill="none" stroke="var(--line-blue)" stroke-width="2"
                points="272,0 272,32 671,32 1050,410"/>
      <polygon fill="var(--navy)" points="0,472 159,314 446,600 0,600"/>
      <polygon fill="var(--red-dark)" points="45,600 157,489 157,600"/>
      <polygon fill="var(--red)" points="157,489 270,600 157,600"/>
    </svg>

    <div class="identity">
      <h1 class="person-name">DANIEL K. HARROWELL</h1>
      <p class="person-title">CHIEF FINANCIAL OFFICER</p>
      <div class="title-rule"></div>
      <p class="tagline">Premier Property Management Solutions</p>
    </div>

    <div class="company-mark">
      <span class="mark-square"></span>
      <span class="company-name">Larkspur Ridge Management</span>
    </div>

    <div class="contact-line">
      <span class="phone">(555) 817-3094</span>
      <svg class="divider-star" viewBox="0 0 24 24" aria-hidden="true">
        <polygon fill="var(--red)" points="12,1 15,9 23,9 16.5,14 19,22 12,17 5,22 7.5,14 1,9 9,9"/>
      </svg>
      <span class="website">larkridgemgmt.example</span>
    </div>
  </div>
</body>
</html>
```